Criação de Papelaria Profissional para Beleza
A empresa queria:
" Espaço físico tipo loja com cabines exclusivas para depilação, método Espanhol com cera quente. Única com cauterização pós depilação. E espaço dedicado a beleza das mãos e pés "

```html
<!DOCTYPE html>
<html lang="pt-BR">
<head>
<meta charset="UTF-8">
<title>Assinatura de e-mail – Alvina</title>
<link rel="stylesheet" href="https://fonts.googleapis.com/css2?family=Montserrat:wght@400;500;700&display=swap">
<style>
  :root {
    --page-bg: #efefef;
    --card-bg: #ffffff;
    --brand-pink: #ec4a8a;
    --brand-pink-light: #f6a9c8;
    --text-dark: #1f1f1f;
    --text-muted: #707070;
    --on-pink: #ffffff;
  }
  * { box-sizing: border-box; margin: 0; padding: 0; }
  html, body {
    width: 1200px;
    height: 1200px;
    overflow: hidden;
    background: var(--page-bg);
    font-family: "Montserrat", Arial, sans-serif;
  }
  .signature {
    position: absolute;
    left: 50px;
    top: 466px;
    width: 1100px;
    height: 268px;
    background: var(--card-bg);
    overflow: hidden;
  }
  .signature__shape {
    position: absolute;
    inset: 0;
  }
  .identity {
    position: absolute;
    left: 46px;
    top: 34px;
    padding-left: 16px;
    border-left: 6px solid var(--brand-pink);
  }
  .identity__name {
    font-size: 25px;
    font-weight: 500;
    color: var(--text-dark);
    line-height: 30px;
    letter-spacing: 0.2px;
  }
  .identity__role {
    font-size: 19px;
    color: var(--text-muted);
    line-height: 28px;
  }
  .identity__role span { color: var(--brand-pink); padding: 0 4px; }
  .contacts {
    position: absolute;
    left: 46px;
    top: 112px;
    list-style: none;
  }
  .contacts__item {
    display: flex;
    align-items: flex-start;
    gap: 12px;
    height: 34px;
    font-size: 17px;
    font-weight: 500;
    color: var(--text-dark);
    line-height: 20px;
  }
  .contacts__item--address { line-height: 18px; height: auto; }
  .contacts__icon {
    flex: none;
    width: 20px;
    height: 20px;
  }
  .brand {
    position: absolute;
    left: 760px;
    top: 0;
    width: 300px;
    height: 268px;
    display: flex;
    align-items: center;
    justify-content: center;
    gap: 14px;
  }
  .brand__dot {
    width: 22px;
    height: 22px;
    border-radius: 50%;
    background: var(--on-pink);
  }
  .brand__name {
    font-size: 62px;
    font-weight: 500;
    color: var(--on-pink);
    letter-spacing: 2px;
    text-transform: lowercase;
  }
</style>
</head>
<body>
  <div class="signature">
    <svg class="signature__shape" width="1100" height="268" viewBox="0 0 1100 268" aria-hidden="true">
      <path d="M424 0 Q450 200 660 268 L700 268 Q472 200 452 0 Z" fill="var(--brand-pink-light)"/>
      <path d="M444 0 Q470 200 700 268 L1100 268 L1100 0 Z" fill="var(--brand-pink)"/>
    </svg>

    <div class="identity">
      <p class="identity__name">NOME E SOBRENOME</p>
      <p class="identity__role">Cargo<span>|</span>Função</p>
    </div>

    <ul class="contacts">
      <li class="contacts__item">
        <svg class="contacts__icon" viewBox="0 0 20 20" aria-hidden="true">
          <circle cx="10" cy="10" r="10" fill="var(--brand-pink)"/>
          <path d="M6.5 5.5 L8.2 5.2 L9 7.6 L8 8.6 Q9 10.8 11.4 12 L12.4 11 L14.8 11.8 L14.5 13.5 Q13.8 14.6 12 14.3 Q7.4 13 5.7 8 Q5.4 6.3 6.5 5.5 Z" fill="#fff"/>
        </svg>
        (00) 0000-0000
      </li>
      <li class="contacts__item">
        <svg class="contacts__icon" viewBox="0 0 20 20" aria-hidden="true">
          <circle cx="10" cy="10" r="10" fill="var(--brand-pink)"/>
          <rect x="5" y="6.5" width="10" height="7" rx="1" fill="#fff"/>
          <path d="M5.5 7 L10 10.5 L14.5 7" fill="none" stroke="var(--brand-pink)" stroke-width="1"/>
        </svg>
        contato@exemplo.com
      </li>
      <li class="contacts__item">
        <svg class="contacts__icon" viewBox="0 0 20 20" aria-hidden="true">
          <circle cx="10" cy="10" r="10" fill="var(--brand-pink)"/>
          <circle cx="10" cy="10" r="5" fill="none" stroke="#fff" stroke-width="1.3"/>
          <ellipse cx="10" cy="10" rx="2.2" ry="5" fill="none" stroke="#fff" stroke-width="1.1"/>
          <path d="M5 10 H15" stroke="#fff" stroke-width="1.1"/>
        </svg>
        www.exemplo.com.br
      </li>
      <li class="contacts__item contacts__item--address">
        <svg class="contacts__icon" viewBox="0 0 20 20" aria-hidden="true">
          <circle cx="10" cy="10" r="10" fill="var(--brand-pink)"/>
          <path d="M10 15.5 Q6 11 6 8.5 A4 4 0 0 1 14 8.5 Q14 11 10 15.5 Z" fill="#fff"/>
          <circle cx="10" cy="8.5" r="1.5" fill="var(--brand-pink)"/>
        </svg>
        <span>rua exemplo, sl 000<br>cidade-UF, CEP: 00000-000</span>
      </li>
    </ul>

    <div class="brand">
      <span class="brand__dot"></span>
      <span class="brand__name">alvina</span>
    </div>
  </div>
</body>
</html>
```